Plumbing Truck design, emergency plumbing vehicle

Simple, highly effective plumbing design for plumbing vehicles

Brightwater Plumbing & Gas Services
(The Steadfast Pipe Professionals) moto

yellow, black and white colours (white as the vehicles are already painted white)

Clean and simple design

Attention grabbing

24hr Emergency service (listed on on the vehicle) possibly in red colour

Target Market(s)

plumbing

Industry/Entity Type

Plumbing

Colors
fbed22

Requirements
Must have
• Brightwater Plumbing & Gas Services
• (The Steadfast Pipe Professionals) moto
• yellow, black and white colours (white as the vehicles are already painted white)
• Clean and simple design
• Attention grabbing
• 24hr Emergency service (listed on on the vehicle) possibly in red colour
Should not have
• No plumbing symbols, pictures or icons

```html
<!DOCTYPE html>
<html lang="en">
<head>
<meta charset="utf-8">
<title>Brightwater Plumbing &amp; Gas Services – Vehicle Wrap Panels</title>
<link href="https://fonts.googleapis.com/css2?family=Archivo+Black&family=Bowlby+One&family=Titan+One&display=swap" rel="stylesheet">
<style>
  :root {
    --brand-yellow: #fbed22;
    --brand-black: #000000;
    --brand-white: #ffffff;
    --alert-red: #e3161d;
    --frame-grey: #b9bcc0;
    --page-bg: #ffffff;
  }
  html, body {
    margin: 0;
    width: 1200px;
    height: 1200px;
    overflow: hidden;
    background: var(--page-bg);
  }
  .wrap-sheet {
    position: relative;
    width: 1200px;
    height: 1200px;
  }
  .panel {
    position: absolute;
    display: block;
  }
  .panel--side-upper { left: 42px;  top: 180px; width: 532px; height: 250px; }
  .panel--side-lower { left: 218px; top: 638px; width: 532px; height: 250px; }
  .panel--front      { left: 914px; top: 178px; width: 226px; height: 88px; }
  .panel--rear       { left: 910px; top: 638px; width: 226px; height: 256px; }

  .fill-yellow { fill: var(--brand-yellow); }
  .fill-black  { fill: var(--brand-black); }

  .emergency-number {
    font-family: "Bowlby One", sans-serif;
    fill: var(--alert-red);
    stroke: var(--brand-black);
    stroke-width: 1.5px;
    paint-order: stroke;
  }
  .emergency-label {
    font-family: "Bowlby One", sans-serif;
    fill: var(--alert-red);
  }
  .brand-name {
    font-family: "Archivo Black", sans-serif;
    fill: var(--brand-white);
    text-anchor: middle;
  }
  .tagline {
    font-family: "Titan One", sans-serif;
    fill: var(--brand-yellow);
    stroke: var(--brand-black);
    stroke-width: 4px;
    stroke-linejoin: round;
    paint-order: stroke;
  }
  .door-frame { fill: none; stroke: var(--frame-grey); stroke-width: 3; }
  .door-seam  { stroke: var(--frame-grey); stroke-width: 3; }
</style>
</head>
<body>
<main class="wrap-sheet">

  <!-- Driver side box panel -->
  <svg class="panel panel--side-upper" viewBox="0 0 443 208" preserveAspectRatio="none" aria-label="Box side panel">
    <defs>
      <radialGradient id="burst-upper" cx="0.12" cy="0.35" r="0.5">
        <stop offset="0" stop-color="#ffffff"/>
        <stop offset="0.6" stop-color="#ffffff"/>
        <stop offset="1" stop-color="#fbed22" stop-opacity="0"/>
      </radialGradient>
    </defs>
    <rect class="fill-yellow" width="443" height="208"/>
    <rect role="img" aria-label="White sunburst rays behind the emergency banner" width="443" height="208" fill="url(#burst-upper)"/>
    <polygon class="fill-black" points="0,142 200,104 443,82 443,208 0,208"/>
    <g class="emergency-banner" transform="translate(6 80) rotate(-14)">
      <text class="emergency-number" x="0" y="-18" font-size="34">24</text>
      <text class="emergency-label" x="50" y="-26" font-size="11">HOURS</text>
      <text class="emergency-label" x="0" y="0" font-size="15">EMERGENCY SERVICE</text>
    </g>
    <g class="brand-block">
      <rect class="fill-black" x="137" y="58" width="166" height="66" rx="6"/>
      <text class="brand-name" x="220" y="88" font-size="21">Brightwater</text>
      <text class="brand-name" x="220" y="110" font-size="10">Plumbing &amp; Gas Services</text>
    </g>
    <g class="tagline-block">
      <text class="tagline" transform="translate(88 184) rotate(-11)" font-size="24">The Steadfast Pipe</text>
      <text class="tagline" transform="translate(220 186) rotate(-11)" font-size="24">Professionals</text>
    </g>
  </svg>

  <!-- Passenger side box panel -->
  <svg class="panel panel--side-lower" viewBox="0 0 443 208" preserveAspectRatio="none" aria-label="Box side panel">
    <defs>
      <radialGradient id="burst-lower" cx="0.12" cy="0.35" r="0.5">
        <stop offset="0" stop-color="#ffffff"/>
        <stop offset="0.6" stop-color="#ffffff"/>
        <stop offset="1" stop-color="#fbed22" stop-opacity="0"/>
      </radialGradient>
    </defs>
    <rect class="fill-yellow" width="443" height="208"/>
    <rect role="img" aria-label="White sunburst rays behind the emergency banner" width="443" height="208" fill="url(#burst-lower)"/>
    <polygon class="fill-black" points="0,142 200,104 443,82 443,208 0,208"/>
    <g class="emergency-banner" transform="translate(6 80) rotate(-14)">
      <text class="emergency-number" x="0" y="-18" font-size="34">24</text>
      <text class="emergency-label" x="50" y="-26" font-size="11">HOURS</text>
      <text class="emergency-label" x="0" y="0" font-size="15">EMERGENCY SERVICE</text>
    </g>
    <g class="brand-block">
      <rect class="fill-black" x="137" y="58" width="166" height="66" rx="6"/>
      <text class="brand-name" x="220" y="88" font-size="21">Brightwater</text>
      <text class="brand-name" x="220" y="110" font-size="10">Plumbing &amp; Gas Services</text>
    </g>
    <g class="tagline-block">
      <text class="tagline" transform="translate(88 184) rotate(-11)" font-size="24">The Steadfast Pipe</text>
      <text class="tagline" transform="translate(220 186) rotate(-11)" font-size="24">Professionals</text>
    </g>
  </svg>

  <!-- Front header panel above the cab -->
  <svg class="panel panel--front" viewBox="0 0 188 73" aria-label="Box front header panel">
    <rect class="fill-yellow" width="188" height="73"/>
    <rect class="fill-black" y="40" width="188" height="33"/>
    <g class="brand-block">
      <rect class="fill-black" x="46" y="20" width="96" height="42" rx="4"/>
      <text class="brand-name" x="94" y="39" font-size="12">Brightwater</text>
      <text class="brand-name" x="94" y="53" font-size="6.2">Plumbing &amp; Gas Services</text>
    </g>
  </svg>

  <!-- Rear doors panel -->
  <svg class="panel panel--rear" viewBox="0 0 188 213" aria-label="Rear doors panel">
    <rect class="fill-yellow" width="188" height="213"/>
    <rect class="fill-black" y="106" width="188" height="107"/>
    <rect class="door-frame" x="1.5" y="1.5" width="185" height="210"/>
    <line class="door-seam" x1="94" y1="0" x2="94" y2="213"/>
    <g class="brand-block">
      <rect class="fill-black" x="16" y="74" width="156" height="64" rx="5"/>
      <text class="brand-name" x="94" y="103" font-size="19">Brightwater</text>
      <text class="brand-name" x="94" y="124" font-size="9.5">Plumbing &amp; Gas Services</text>
    </g>
  </svg>

</main>
</body>
</html>
```